Corvenne Jewelers Business Cards

A creative, cool edgy business card for our entire team that says we are a young, hip, luxury jewelry store specializing in diamonds and engagement rings but that we are also personal shoppers and trusted advisors. Our colors are Navy Blue & Platinum

I have included our past business card.

Font styles to use
Serif

Colors
0255a3

Requirements
Nice to have
• A card stock that you can write on with a pen

```html
<!DOCTYPE html>
<html lang="en">
<head>
<meta charset="utf-8">
<title>Corvenne Jewelers Business Cards</title>
<link href="https://fonts.googleapis.com/css2?family=Cormorant+SC:wght@600&family=Rokkitt:wght@600&family=Lato:wght@400&display=swap" rel="stylesheet">
<style>
  :root {
    --navy: #14215e;
    --navy-deep: #101a4d;
    --platinum: #e9e8e6;
    --ink: #1c1c1c;
    --rule: #c9c8c6;
    --backdrop: #d9d9d9;
  }
  * { margin: 0; padding: 0; box-sizing: border-box; }
  html, body { width: 1200px; height: 782px; overflow: hidden; }
  body {
    background: var(--backdrop);
    display: flex;
    align-items: center;
    justify-content: center;
    gap: 60px;
  }
  .card {
    width: 520px;
    height: 297px;
    position: relative;
    box-shadow: 0 6px 18px rgba(0,0,0,0.25);
  }
  /* Front */
  .card-front {
    background: var(--platinum);
    display: flex;
    border-bottom: 9px solid var(--navy);
  }
  .brand {
    width: 48%;
    display: flex;
    align-items: center;
    justify-content: center;
    gap: 10px;
  }
  .brand-dot {
    width: 14px; height: 14px;
    border-radius: 50%;
    background: var(--navy);
  }
  .brand-name {
    font-family: "Cormorant SC", serif;
    font-weight: 600;
    font-size: 23px;
    color: var(--navy);
    letter-spacing: 0.5px;
  }
  .divider {
    width: 1px;
    background: var(--rule);
    margin: 70px 0 50px;
  }
  .contact {
    padding: 62px 0 0 30px;
    color: var(--ink);
    font-family: "Lato", sans-serif;
  }
  .person-name {
    font-family: "Rokkitt", serif;
    font-weight: 600;
    font-size: 24px;
    letter-spacing: 1px;
    color: var(--navy);
    line-height: 1;
  }
  .person-title {
    font-size: 15px;
    margin: 2px 0 6px;
  }
  .contact-list { list-style: none; font-size: 15px; line-height: 1.3; }
  .contact-list li { display: flex; align-items: center; gap: 7px; }
  .contact-list svg { width: 12px; height: 12px; fill: var(--navy); flex: none; }
  .address { font-size: 15px; line-height: 1.3; margin-top: 4px; }
  /* Back */
  .card-back {
    background: var(--navy-deep);
    display: flex;
    align-items: center;
    justify-content: center;
  }
  .back-pattern {
    position: absolute; inset: 0;
    background: linear-gradient(135deg, #15225e, #1a2a6c 50%, #15225e);
  }
  .back-name {
    position: relative;
    font-family: "Cormorant SC", serif;
    font-weight: 600;
    font-size: 22px;
    color: #ffffff;
    letter-spacing: 0.5px;
  }
</style>
</head>
<body>
  <section class="card card-front">
    <div class="brand">
      <span class="brand-dot"></span>
      <span class="brand-name">Corvenne Jewelers</span>
    </div>
    <div class="divider"></div>
    <div class="contact">
      <h1 class="person-name">ELIAS MARLOWE</h1>
      <p class="person-title">Managing Director</p>
      <ul class="contact-list">
        <li><svg viewBox="0 0 12 12"><path d="M2 1h3l1 3-1.5 1a6 6 0 0 0 2.5 2.5L8 6l3 1v3c0 .6-.4 1-1 1A9 9 0 0 1 1 2c0-.6.4-1 1-1z"/></svg>044-210 387 615</li>
        <li><svg viewBox="0 0 12 12"><path d="M3 0h6a1 1 0 0 1 1 1v10a1 1 0 0 1-1 1H3a1 1 0 0 1-1-1V1a1 1 0 0 1 1-1zm0 2v7h6V2z"/></svg>044-210 387 615</li>
        <li><svg viewBox="0 0 12 12"><path d="M0 2h12v8H0zm1 1v.5l5 3 5-3V3z"/></svg>info@corvennejewel.com</li>
        <li><svg viewBox="0 0 12 12"><circle cx="6" cy="6" r="6"/></svg>www.corvennejewel.com</li>
      </ul>
      <p class="address">12345, Address Goes Here<br>Country Name, 123456.</p>
    </div>
  </section>
  <section class="card card-back">
    <div class="back-pattern" role="img" aria-label="Faint repeating monogram pattern on navy"></div>
    <span class="back-name">Corvenne Jewelers</span>
  </section>
</body>
</html>
```